Online media outlet needs a blog and logo

A new online blog platform is being established in the UK. The blog will be very similar in layout to www.dravonet.co. It will need to have a main story slider showing three slides and block tiles beneath the slider for additional tiles.

The blog platform will be called 'Tarsel Quill' and will also need a professional looking logo design for the name.

The website should be designed in Word Press.

Industry/Entity Type

Media

Logo Text

Tarsel Quill

Coding

Coded - Design and coding required

Number of Pages Required

3 page

Font styles to use
Other font styles liked:
• Helvetica

Requirements
Must have
• A slider showing three slides. Be similar to Drav N (see previous comment). Be Word Press compatible.

```html
<!DOCTYPE html>
<html lang="en">
<head>
<meta charset="utf-8">
<title>Tarsel Quill</title>
<link rel="stylesheet" href="https://fonts.googleapis.com/css2?family=Raleway:ital,wght@0,400;0,500;0,600;0,700;1,400&display=swap">
<style>
:root{
  --ink:#222;
  --muted:#666;
  --meta:#999;
  --header:#1d2a3c;
  --nav:#333;
  --nav-active:#111;
  --page:#f2f2f2;
  --card:#fff;
  --accent:#21b5e8;
  --blue:#5ec2ee;
  --purple:#6f62d8;
  --green:#69c35a;
  --yellow:#f2c320;
  --news:#2c2c2c;
  --foot:#0d0d0d;
}
*{box-sizing:border-box;margin:0;padding:0}
html,body{width:677px;height:1200px;overflow:hidden}
body{position:relative;font-family:"Raleway",Helvetica,sans-serif;color:var(--ink);background:var(--page)}
.site-header{position:absolute;top:0;left:0;width:677px;height:38px;background:rgba(20,32,50,.92);z-index:2;display:flex;align-items:center;padding:0 50px}
.brand{color:#fff;font-size:17px;font-weight:400;letter-spacing:.3px;text-transform:uppercase}
.header-tools{margin-left:auto;display:flex;align-items:center;gap:6px}
.social-dot{width:13px;height:13px;border-radius:50%;background:#fff}
.menu-toggle{margin-left:12px;color:#fff;font-size:8px;display:flex;align-items:center;gap:5px}
.hero{position:absolute;top:0;left:0;width:677px;height:370px;background:linear-gradient(180deg,#3b8ad8 0%,#8cc0ea 45%,#5b9fc0 72%,#c9a06a 80%,#b8874e 100%)}
.hero-card{position:absolute;left:48px;top:178px;width:223px;height:138px;background:rgba(70,78,88,.82);border-radius:3px;padding:16px 16px;color:#fff}
.hero-cat{font-size:8px;letter-spacing:.3px;display:flex;align-items:center;gap:5px}
.hero-title{font-size:12.5px;font-weight:700;line-height:17px;margin-top:8px}
.hero-text{font-size:8px;line-height:16px;margin-top:8px;color:#e6e6e6}
.hero-more{display:block;margin-top:5px;font-size:8px;font-weight:700;color:var(--accent);text-decoration:none}
.topic-nav{position:absolute;top:370px;left:0;width:677px;height:51px;background:var(--nav);padding-left:50px;display:flex}
.topic-nav a{height:51px;display:flex;align-items:center;justify-content:center;color:#fff;font-size:8.6px;text-decoration:none;border-right:1px solid #444}
.topic-nav a.active{background:var(--nav-active)}
.card{position:absolute;background:var(--card);box-shadow:0 1px 2px rgba(0,0,0,.18);border-top:3px solid var(--blue);overflow:hidden}
.card .photo{position:absolute;display:block}
.tag{position:absolute;top:14px;right:0;background:rgba(40,40,40,.8);color:#fff;font-size:8px;font-weight:700;padding:3px 6px;display:flex;gap:4px;align-items:center}
.body{position:absolute;padding:0 12px}
.title{font-size:9.2px;font-weight:700;line-height:13.5px}
.meta{font-size:6.4px;font-style:italic;color:var(--meta);margin-top:3px}
.rule{border-top:1px solid #eee;margin:8px 0 7px}
.excerpt{font-size:7.2px;line-height:13px;color:var(--muted)}
.share{display:flex;align-items:center;gap:8px;font-size:5.8px;color:#444;margin-top:10px}
.share i{width:6px;height:7px;background:#222;display:inline-block;border-radius:1px}
.newsletter{position:absolute;top:995px;left:0;width:677px;height:173px;background:linear-gradient(180deg,#3a3a3a,#262626);text-align:center;color:#fff}
.newsletter h2{font-weight:400;font-size:21.5px;margin-top:33px}
.newsletter p{font-size:9.2px;margin-top:8px;color:#eee}
.signup{position:absolute;top:100px;left:112px;display:flex;gap:9px}
.field{height:27px;background:#fff;color:#888;font-size:8px;display:flex;align-items:center;padding:0 10px;border-radius:1px}
.subscribe{height:27px;width:70px;background:var(--accent);color:#fff;font-size:8px;font-weight:700;display:flex;align-items:center;justify-content:center;margin-left:0}
.site-footer{position:absolute;top:1168px;left:0;width:677px;height:32px;background:var(--foot);color:#ccc;font-size:7.2px;display:flex;align-items:center;justify-content:center}
.site-footer b{color:#fff}
</style>
</head>
<body>
<header class="site-header">
  <div class="brand">Tarsel Quill</div>
  <div class="header-tools">
    <span class="social-dot"></span><span class="social-dot"></span><span class="social-dot"></span><span class="social-dot"></span>
    <span class="menu-toggle">MENU
      <svg width="12" height="9" viewBox="0 0 12 9"><path d="M0 1h12M0 4.5h12M0 8h12" stroke="#fff" stroke-width="1.3"/></svg>
    </span>
  </div>
</header>

<section class="hero" role="img" aria-label="Beach scene with a coconut, sunglasses and a striped flip-flop on the sand">
  <article class="hero-card">
    <div class="hero-cat"><svg width="7" height="7" viewBox="0 0 7 7"><path d="M1 6l1-3 3-3 2 2-3 3z" fill="#fff"/></svg>TRAVEL TIPS</div>
    <h1 class="hero-title">Lorem ipsum dolor sit amet, consectetuer adipiscing</h1>
    <p class="hero-text">Lorem ipsum dolor sit amet, consectetuer adipiscing elit, sed diam nonummy nibh [..]</p>
    <a class="hero-more" href="#">READ MORE</a>
  </article>
</section>

<nav class="topic-nav">
  <a class="active" href="#" style="width:108px">CURRENT TOPICS</a>
  <a href="#" style="width:98px">GOVERNMENT</a>
  <a href="#" style="width:76px">POLITICS</a>
  <a href="#" style="width:98px">COMPETITION</a>
  <a href="#" style="width:94px">INVESTMENT</a>
  <a href="#" style="width:104px">SHARE MARKET</a>
</nav>

<article class="card" style="left:50px;top:454px;width:185px;height:326px;border-color:var(--blue)">
  <div class="photo" role="img" aria-label="Firefighter spraying a burning car" style="left:0;top:0;width:185px;height:158px;background:linear-gradient(110deg,#8a8070,#c96a2a 60%,#f0a030)"></div>
  <span class="tag">Breaking News ✎</span>
  <div class="body" style="top:168px;width:185px">
    <h3 class="title">Lorem ipsum dolor sit amet, consectetuer adipiscing elit, sed</h3>
    <div class="meta">Posted On 03 May, 2016</div>
    <div class="rule"></div>
    <p class="excerpt">Lorem ipsum dolor sit amet, consectetuer adipiscing elit, sed diam nonummy nibh euismod tincidunt ut laoreet dolore magna aliquam erat volutpat. Ut wisi enim ad minim veniam, quis nostrud exerci tation sed diam nonummy nibh euismod</p>
    <div class="share">SHARE THIS: <i></i><i></i></div>
  </div>
</article>

<article class="card" style="left:246px;top:454px;width:185px;height:158px;border-color:var(--purple)">
  <div class="photo" role="img" aria-label="Business people in a meeting" style="left:0;top:0;width:185px;height:78px;background:linear-gradient(90deg,#6b5a48,#a08a6e,#4a3f36)"></div>
  <span class="tag">Politics ✎</span>
  <div class="body" style="top:87px;width:185px">
    <h3 class="title">Lorem ipsum dolor sit amet, consectetuer adipiscing elit, sed</h3>
    <div class="meta">Posted On 03 May, 2016</div>
    <div class="share">SHARE THIS: <i></i><i></i></div>
  </div>
</article>

<article class="card" style="left:442px;top:454px;width:186px;height:158px;border-color:var(--green)">
  <div class="photo" role="img" aria-label="Hands reviewing financial charts on paper" style="left:0;top:0;width:186px;height:78px;background:linear-gradient(90deg,#b9bcc0,#e8eaee,#9ea3aa)"></div>
  <span class="tag">Investment ✎</span>
  <div class="body" style="top:87px;width:186px">
    <h3 class="title">Lorem ipsum dolor sit amet, consectetuer adipiscing elit, sed</h3>
    <div class="meta">Posted On 03 May, 2016</div>
    <div class="share">SHARE THIS: <i></i><i></i></div>
  </div>
</article>

<article class="card" style="left:246px;top:623px;width:382px;height:157px;border-color:var(--yellow)">
  <div class="photo" role="img" aria-label="Singer performing with a microphone" style="left:0;top:0;width:186px;height:157px;background:linear-gradient(135deg,#2e5a26,#6aa040 55%,#3b2a22)"></div>
  <span class="tag" style="right:196px">Entertainment ✎</span>
  <div class="body" style="left:186px;top:13px;width:196px">
    <h3 class="title">Lorem ipsum dolor sit amet, consec tetuer adipiscing elit, sed</h3>
    <div class="meta">Posted On 03 May, 2016</div>
    <div class="rule"></div>
    <p class="excerpt">Lorem ipsum dolor sit amet, consectetuer adipiscing elit, sed diam nonummy nibh euismod tincidunt ut laoreet dolore magna aliquam erat volutpat. Ut wisi enim ad minim veniam, quis nostrud exerci tation sed diam nonummy nibh</p>
    <div class="share">SHARE THIS: <i></i><i></i></div>
  </div>
</article>

<article class="card" style="left:50px;top:793px;width:381px;height:157px;border-color:var(--green)">
  <div class="photo" role="img" aria-label="Blue stock market chart on a screen" style="left:0;top:0;width:185px;height:157px;background:linear-gradient(160deg,#0c2a6e,#1d55c0 55%,#0a1c4a)"></div>
  <span class="tag" style="right:196px;top:20px">Share Market ✎</span>
  <div class="body" style="left:185px;top:13px;width:196px">
    <h3 class="title">Lorem ipsum dolor sit amet, consec tetuer adipiscing elit, sed</h3>
    <div class="meta">Posted On 03 May, 2016</div>
    <div class="rule"></div>
    <p class="excerpt">Lorem ipsum dolor sit amet, consectetuer adipiscing elit, sed diam nonummy nibh euismod tincidunt ut laoreet dolore magna aliquam erat volutpat. Ut wisi enim ad minim veniam, quis nostrud exerci tation sed diam nonummy nibh</p>
    <div class="share">SHARE THIS: <i></i><i></i></div>
  </div>
</article>

<article class="card" style="left:442px;top:793px;width:186px;height:157px;border-color:var(--blue)">
  <div class="photo" role="img" aria-label="Aerial view of a waterfront city" style="left:0;top:0;width:186px;height:78px;background:linear-gradient(180deg,#8fb5d6,#6b7e8c 50%,#4a5560)"></div>
  <span class="tag">Property ✎</span>
  <div class="body" style="top:87px;width:186px">
    <h3 class="title">Lorem ipsum dolor sit amet, consectetuer adipiscing elit, sed</h3>
    <div class="meta">Posted On 03 May, 2016</div>
    <div class="share">SHARE THIS: <i></i><i></i></div>
  </div>
</article>

<section class="newsletter" role="img" aria-label="Dark city skyline backdrop behind the newsletter sign-up">
  <h2>Tarsel Quill Newsletter Sign Up</h2>
  <p>Sign up to our email briefings to have the best of popular capitalism delivered direct to your inbox.</p>
  <form class="signup">
    <div class="field" style="width:265px">Email Address</div>
    <div class="field" style="width:100px;justify-content:space-between">Daily
      <svg width="9" height="6" viewBox="0 0 9 6"><path d="M1 1l3.5 3.5L8 1" stroke="#444" stroke-width="1.2" fill="none"/></svg>
    </div>
    <div class="subscribe">SUBSCRIBE</div>
  </form>
</section>

<footer class="site-footer">Copyright © 2016&nbsp;<b>Tarsel Quill</b>&nbsp;| All Rights Reserved.</footer>
</body>
</html>
```